Simple, Professional and neat business card design for Vendralo Inc.

We're looking to re-vamp our business card design. We're a supplier of innovative feed ingredients for the North American animal agriculture industry. We are located in Lucknow, Ontario, Canada and our flagship product is a product that prevents milk fever in dairy cows when the calve, it is fed before calving and is very effective compared to other alternatives available on the market today.

Our company has Danish roots and we import all of our product from our Danish partner/manufacturer in Denmark. We like our design to embrace high professionalism while remaining neat and simple.

Target Market(s)

B2B, Feed Mills, Veterinary Clinics, Large integrators/producers,

Industry/Entity Type

Agribusiness

Contact Information for Business Card

We like the rounded corners because they make the card easy to sit in a wallet and not many use it so it makes the card stand out, just possibly something to take account for during the design.

As you can also see on the sliders below, looking for a that simple but proffesional scandinavian design.

Requirements
Nice to have
• Rounded corners
Should not have
• Too vibrant

```html
<!DOCTYPE html>
<html lang="en">
<head>
<meta charset="utf-8">
<title>Vendralo Inc. — Business Card</title>
<link href="https://fonts.googleapis.com/css2?family=Cinzel:wght@500;600&family=Open+Sans:wght@400;600&family=Source+Sans+3:wght@700;800&display=swap" rel="stylesheet">
<style>
  :root{
    --bg:#e8e9eb;
    --card:#f6f6f5;
    --blue:#1f4a9c;
    --gold:#b8964a;
    --ink:#222;
    --pattern:#dcdcda;
  }
  *{box-sizing:border-box;margin:0;padding:0}
  html,body{width:1200px;height:800px;overflow:hidden;background:var(--bg)}
  .stage{width:1200px;height:800px;display:flex;align-items:center;justify-content:center;gap:40px}
  .card{position:relative;width:540px;height:310px;background:var(--card);border-radius:10px;box-shadow:0 10px 24px rgba(0,0,0,.12);overflow:hidden}

  /* front */
  .animal-pattern{position:absolute;inset:0;background:radial-gradient(circle at 30% 30%,var(--pattern),transparent 60%),radial-gradient(circle at 75% 70%,var(--pattern),transparent 60%);opacity:.7}
  .front-brand{position:absolute;left:0;right:0;top:118px;display:flex;align-items:center;justify-content:center;gap:14px}
  .brand-dot{width:44px;height:44px;border-radius:50%;background:var(--blue)}
  .brand-dot.small{width:26px;height:26px}
  .brand-name{font-family:"Source Sans 3",sans-serif;font-weight:800;color:var(--blue);font-size:40px;letter-spacing:.5px;text-transform:uppercase}
  .socials{position:absolute;left:0;right:0;top:196px;display:flex;justify-content:center;gap:26px;font-family:"Open Sans",sans-serif;font-size:11px;color:var(--gold)}
  .socials li{list-style:none;display:flex;align-items:center;gap:6px}
  .socials li::before{content:"";width:10px;height:10px;border-radius:50%;background:var(--gold)}

  /* back */
  .back-brand{position:absolute;left:36px;top:118px;display:flex;align-items:center;gap:10px}
  .back-brand .brand-name{font-size:22px}
  .person{position:absolute;left:36px;top:210px}
  .person-name{font-family:"Cinzel",serif;font-weight:600;color:var(--gold);font-size:19px;letter-spacing:.5px}
  .person-role{font-family:"Cinzel",serif;font-weight:500;color:var(--ink);font-size:12px;margin-top:2px;letter-spacing:.5px}
  .contact{position:absolute;left:310px;top:52px;font-family:"Open Sans",sans-serif;font-size:11.5px;color:var(--gold);line-height:1.55}
  .contact-group{margin-bottom:18px}
  .row{display:flex;align-items:flex-start;gap:8px}
  .row svg{width:11px;height:11px;flex:none;margin-top:3px;fill:var(--gold)}
  .row.blank{padding-left:19px}
</style>
</head>
<body>
<main class="stage">
  <section class="card card-front">
    <div class="animal-pattern" role="img" aria-label="Faint pattern of farm and wild animal silhouettes"></div>
    <div class="front-brand">
      <span class="brand-dot"></span>
      <span class="brand-name">Vendralo Inc.</span>
    </div>
    <ul class="socials">
      <li>VendraloINC</li>
      <li>VendraloINC</li>
      <li>VendraloINC</li>
    </ul>
  </section>

  <section class="card card-back">
    <div class="back-brand">
      <span class="brand-dot small"></span>
      <span class="brand-name">Vendralo Inc.</span>
    </div>
    <div class="person">
      <p class="person-name">MIKKEL THORSEN</p>
      <p class="person-role">MANAGER</p>
    </div>
    <div class="contact">
      <div class="contact-group">
        <div class="row"><svg viewBox="0 0 12 12"><path d="M6 0a4 4 0 0 0-4 4c0 3 4 8 4 8s4-5 4-8a4 4 0 0 0-4-4zm0 5.5A1.5 1.5 0 1 1 6 2.5a1.5 1.5 0 0 1 0 3z"/></svg><span>Box 412, Northfield,</span></div>
        <div class="row blank">ON, Canada N0H 3K0</div>
      </div>
      <div class="contact-group">
        <div class="row"><svg viewBox="0 0 12 12"><rect x="3" y="0" width="6" height="12" rx="1"/><rect x="4" y="1.5" width="4" height="7" fill="#f6f6f5"/></svg><span>+1 555 214 0381</span></div>
        <div class="row"><svg viewBox="0 0 12 12"><path d="M2.5 1l2 2-1 1.5a7 7 0 0 0 4 4L9 7.5l2 2-1.5 1.5C5 11 1 7 1 2.5z"/></svg><span>+1 555 214 0726</span></div>
        <div class="row"><svg viewBox="0 0 12 12"><path d="M2.5 1l2 2-1 1.5a7 7 0 0 0 4 4L9 7.5l2 2-1.5 1.5C5 11 1 7 1 2.5z"/></svg><span>+1 800 555 0149</span></div>
        <div class="row"><svg viewBox="0 0 12 12"><path d="M2.5 1l2 2-1 1.5a7 7 0 0 0 4 4L9 7.5l2 2-1.5 1.5C5 11 1 7 1 2.5z"/></svg><span>+1 555 214 0990</span></div>
      </div>
      <div class="contact-group">
        <div class="row"><svg viewBox="0 0 12 12"><circle cx="6" cy="6" r="5" fill="none" stroke="#b8964a" stroke-width="1.4"/><path d="M1 6h10M6 1c-2 3-2 7 0 10M6 1c2 3 2 7 0 10" fill="none" stroke="#b8964a"/></svg><span>www.vendralo.com</span></div>
        <div class="row"><svg viewBox="0 0 12 12"><rect x="0" y="2" width="12" height="8" rx="1"/><path d="M0 2.5l6 4 6-4" fill="none" stroke="#f6f6f5" stroke-width="1"/></svg><span>mikkel@vendralo.com</span></div>
      </div>
    </div>
  </section>
</main>
</body>
</html>
```